Business Card Design

Consultation for design, construction athletic facilities specializing in synthetic turf systems and all weather running track systems.
Motto "True Owner Representation"
New Company that we'd like to highlight the LOGO first and foremost with the colors of the background and font as primary colors of the card too if possible. I've also attached a typical larger project design layout that could be used in the background to highlight our design and construction specialty.
Website is something we want very noticeable for driving traffic.
Target Market(s)
Athletic Directors, Designers, Government and Military, Contractors
Industry/Entity Type
Construction
Contact Information for Business Card
Peter K. Halvorsen CFD, CTD
48213 W 37th Ave
Pine Hollow, WA 99512
C +1 555.214.7730
O +1 555.381.4062
Peter@fieldlanepro.com
www.fieldlanepro.com
Look and feel
Each slider illustrates characteristics of the customer's brand and the style your logo design should communicate.

```html
<!DOCTYPE html>
<html lang="en">
<head>
<meta charset="UTF-8">
<title>Velora Sport — Business Card</title>
<link rel="stylesheet" href="https://fonts.googleapis.com/css2?family=Open+Sans:wght@400;600&display=swap">
<style>
  :root {
    --bg: #a7a7a9;
    --card-black: #050505;
    --orange: #f7941d;
    --paper: #ffffff;
    --plan-tint: #f6dccb;
    --ink-dark: #1a1208;
  }
  * { box-sizing: border-box; margin: 0; padding: 0; }
  html, body { width: 1200px; height: 900px; overflow: hidden; }
  body {
    background: var(--bg);
    font-family: "Open Sans", Arial, sans-serif;
    position: relative;
  }

  /* ---------- Front of card ---------- */
  .card-front {
    position: absolute;
    left: 70px; top: 300px;
    width: 560px; height: 320px;
    background: var(--card-black);
    box-shadow: 0 10px 24px rgba(0,0,0,.35);
    color: var(--orange);
  }
  .brand-name {
    font-family: "Open Sans", Arial, sans-serif;
    font-weight: 400;
    color: var(--orange);
    line-height: 1;
    white-space: nowrap;
  }
  .card-front .brand-name {
    position: absolute;
    left: 306px; top: 48px;
    font-size: 28px;
  }
  .person {
    position: absolute;
    left: 30px; top: 112px;
    width: 246px;
    text-align: right;
  }
  .person-name {
    font-weight: 600;
    font-size: 22px;
    color: var(--orange);
    white-space: nowrap;
  }
  .person-credentials {
    font-size: 13px;
    margin-top: 6px;
  }
  .divider {
    position: absolute;
    left: 290px; top: 110px;
    width: 1px; height: 80px;
    background: linear-gradient(to bottom, transparent, var(--orange), transparent);
  }
  .contact-details {
    position: absolute;
    left: 306px; top: 114px;
    font-size: 12.5px;
    line-height: 1.55;
    color: var(--orange);
    white-space: nowrap;
  }
  .contact-band {
    position: absolute;
    left: 0; top: 212px;
    width: 100%; height: 38px;
    background: var(--orange);
    display: flex; align-items: center; justify-content: space-around;
    color: var(--ink-dark);
    font-size: 14px;
  }
  .contact-band span { display: inline-flex; align-items: center; gap: 7px; }
  .tagline {
    position: absolute;
    left: 0; top: 270px; width: 100%;
    text-align: center;
    font-size: 13px;
    color: var(--orange);
  }

  /* ---------- Back of card ---------- */
  .card-back {
    position: absolute;
    left: 800px; top: 160px;
    width: 320px; height: 560px;
    background: var(--paper);
    box-shadow: 0 10px 24px rgba(0,0,0,.35);
    overflow: hidden;
  }
  .back-header {
    height: 112px;
    background: var(--card-black);
    display: flex; align-items: center; justify-content: center;
  }
  .back-header .brand-name { font-size: 24px; }
  .notes-label {
    position: absolute;
    left: 20px; top: 126px;
    font-size: 13px;
    color: var(--orange);
  }
  .site-plan {
    position: absolute;
    left: 20px; top: 156px;
    width: 280px; height: 310px;
    background: radial-gradient(ellipse at 50% 45%, var(--plan-tint) 0%, rgba(246,220,203,.45) 55%, rgba(255,255,255,0) 80%);
  }
  .back-footer {
    position: absolute;
    left: 0; bottom: 0;
    width: 100%; height: 76px;
    background: var(--card-black);
    display: flex; align-items: center; justify-content: center;
    color: var(--orange);
    font-size: 14px;
  }
</style>
</head>
<body>

  <section class="card-front">
    <span class="brand-name">Velora Sport</span>

    <div class="person">
      <div class="person-name">Peter K. Halvorsen</div>
      <div class="person-credentials">CFD, CTD</div>
    </div>

    <div class="divider"></div>

    <div class="contact-details">
      <div>C +1 555.214.7730</div>
      <div>O +1 555.381.4062</div>
      <div>48213 W 37th Ave</div>
      <div>Pine Hollow, WA 99512</div>
    </div>

    <div class="contact-band">
      <span>
        <svg width="15" height="11" viewBox="0 0 15 11" aria-hidden="true">
          <rect x="0.5" y="0.5" width="14" height="10" fill="none" stroke="currentColor"/>
          <path d="M0.5 0.5 L7.5 6 L14.5 0.5 M0.5 10.5 L5.5 5 M14.5 10.5 L9.5 5" fill="none" stroke="currentColor"/>
        </svg>
        Peter@fieldlanepro.com
      </span>
      <span>
        <svg width="13" height="13" viewBox="0 0 13 13" aria-hidden="true">
          <circle cx="6.5" cy="6.5" r="6" fill="currentColor"/>
          <path d="M0.5 6.5 H12.5 M6.5 0.5 C3 4 3 9 6.5 12.5 M6.5 0.5 C10 4 10 9 6.5 12.5" fill="none" stroke="var(--orange)" stroke-width="0.9"/>
        </svg>
        www.fieldlanepro.com
      </span>
    </div>

    <div class="tagline">Sports Facility Consulting</div>
  </section>

  <section class="card-back">
    <div class="back-header">
      <span class="brand-name">Velora Sport</span>
    </div>
    <div class="notes-label">Notes</div>
    <div class="site-plan" role="img" aria-label="Faint technical site plan of an athletic complex with running track, field and baseball diamond"></div>
    <div class="back-footer">www.fieldlanepro.com</div>
  </section>

</body>
</html>
```